Business Card Design Project

We need a buisness card for a new digital sinage company. Our target cliants are small to mediaum buisness who want to advertise on out digital sinage network

Target Market(s)

Small to medium buisness

Industry/Entity Type

Digital

Requirements
Must have
• Must have logo

```html
<!DOCTYPE html>
<html lang="en">
<head>
<meta charset="utf-8">
<title>Quorvane Business Card</title>
<link rel="stylesheet" href="https://fonts.googleapis.com/css2?family=Lato:wght@400;700;900&display=swap">
<style>
  :root {
    --blue: #1a8fd6;
    --green: #6aa82c;
    --orange: #f5a51a;
    --ink: #333333;
    --ink-soft: #444444;
    --paper: #ffffff;
    --backdrop: #e4e8ea;
  }
  * { box-sizing: border-box; margin: 0; padding: 0; }
  html, body {
    width: 1200px;
    height: 960px;
    overflow: hidden;
    background: var(--backdrop);
    font-family: "Lato", sans-serif;
  }
  .card {
    position: absolute;
    left: 260px;
    width: 680px;
    height: 390px;
    overflow: hidden;
    box-shadow: 0 10px 30px rgba(0, 0, 0, 0.18);
  }

  /* Front */
  .card-front { top: 50px; background: var(--paper); color: var(--ink); }
  .edge-stripe {
    position: absolute; left: 0; top: 0; bottom: 0; width: 20px;
    display: flex; flex-direction: column;
  }
  .edge-stripe span { flex: 1; }
  .edge-stripe .blue { background: var(--blue); }
  .edge-stripe .green { background: var(--green); }
  .edge-stripe .orange { background: var(--orange); }

  .identity { position: absolute; left: 62px; top: 108px; }
  .person-name { font-size: 30px; font-weight: 400; letter-spacing: 0.5px; text-transform: uppercase; }
  .person-role { font-size: 17px; margin-top: 4px; color: var(--ink-soft); }

  .brand { position: absolute; right: 40px; top: 78px; display: flex; align-items: center; gap: 12px; }
  .brand-square { width: 40px; height: 40px; background: var(--green); flex: none; }
  .brand-name { font-size: 48px; font-weight: 900; color: var(--ink); line-height: 1; }

  .contacts { position: absolute; left: 62px; bottom: 42px; list-style: none; }
  .contacts li { display: flex; align-items: center; gap: 14px; font-size: 20px; line-height: 30px; }
  .contacts svg { width: 18px; height: 18px; flex: none; }

  .address {
    position: absolute; right: 40px; bottom: 72px;
    font-size: 17px; line-height: 24px; font-style: normal; color: var(--ink);
  }
  .address .web { font-weight: 700; }

  /* Back */
  .card-back { top: 520px; display: flex; flex-direction: column; }
  .band-blue { height: 22%; background: var(--blue); }
  .band-green { height: 33%; background: var(--green); }
  .band-orange { flex: 1; background: var(--orange); }
  .back-brand {
    position: absolute; left: 0; right: 0; top: 100px;
    display: flex; justify-content: center; align-items: center; gap: 16px;
  }
  .back-brand .brand-square { background: var(--paper); width: 50px; height: 50px; }
  .back-brand .brand-name { color: var(--paper); font-size: 60px; }
  .back-web {
    position: absolute; left: 0; right: 0; bottom: 38px;
    text-align: center; color: var(--paper); font-size: 16px; letter-spacing: 1px;
  }
</style>
</head>
<body>

<section class="card card-front">
  <div class="edge-stripe"><span class="blue"></span><span class="green"></span><span class="orange"></span></div>

  <div class="brand">
    <span class="brand-square"></span>
    <span class="brand-name">Quorvane</span>
  </div>

  <div class="identity">
    <h1 class="person-name">Nadia Holloway</h1>
    <p class="person-role">Operation Manager</p>
  </div>

  <ul class="contacts">
    <li>
      <svg viewBox="0 0 18 18" aria-hidden="true"><rect x="1" y="2" width="16" height="14" rx="2" fill="none" stroke="#1a8fd6" stroke-width="2"/><rect x="4" y="5" width="4" height="8" fill="#1a8fd6"/><rect x="10" y="5" width="4" height="2" fill="#1a8fd6"/><rect x="10" y="9" width="4" height="2" fill="#1a8fd6"/></svg>
      (221) 30 555 01 12
    </li>
    <li>
      <svg viewBox="0 0 18 18" aria-hidden="true"><rect x="4" y="1" width="10" height="16" rx="2" fill="#6aa82c"/><rect x="6" y="3" width="6" height="5" fill="#ffffff"/></svg>
      (221) 70 555 01 48
    </li>
    <li>
      <svg viewBox="0 0 18 18" aria-hidden="true"><rect x="1" y="4" width="16" height="11" fill="none" stroke="#f5a51a" stroke-width="2"/><path d="M1 4 L9 11 L17 4" fill="none" stroke="#f5a51a" stroke-width="2"/></svg>
      name@quorvane.com
    </li>
  </ul>

  <address class="address">
    Rue des Palmiers - Plateau<br>
    BP 120 - City, Country<br>
    <span class="web">www.quorvane.com</span>
  </address>
</section>

<section class="card card-back">
  <div class="band-blue"></div>
  <div class="band-green"></div>
  <div class="band-orange"></div>
  <div class="back-brand">
    <span class="brand-square"></span>
    <span class="brand-name">Quorvane</span>
  </div>
  <p class="back-web">www.quorvane.com</p>
</section>

</body>
</html>
```